Plush Dwellings website

full website from start to finish. I would like something like this -
https://www.quarrybendmanors.example/
http://tidalcrestvillas.example/

Target Market(s)

real estate investors

Industry/Entity Type

Real Estate

Number of Pages Required

5+ page

Font styles to use
Sans Serif

Colors

Designer to choose colors to be used in the design.

Requirements
Must have
• translated in English, Spanish and japanese

```html
<!DOCTYPE html>
<html lang="en">
<head>
<meta charset="utf-8">
<title>Plush Dwellings — Website Design</title>
<link href="https://fonts.googleapis.com/css2?family=Montserrat:wght@400;500;600;700;800&family=Playfair+Display:wght@700&display=swap" rel="stylesheet">
<style>
:root{
  --bg:#eeeef2;
  --white:#ffffff;
  --ink:#2b2b2f;
  --muted:#8a8a92;
  --faint:#f1f1f3;
  --red:#d42b2b;
  --dark:#26262b;
  --panel:#ececef;
  --foot:#f7f7f9;
}
*{margin:0;padding:0;box-sizing:border-box}
html,body{width:1200px;height:1200px;overflow:hidden}
body{background:var(--bg);font-family:'Montserrat',sans-serif;color:var(--ink);position:relative}
.abs{position:absolute}
.brand-title{left:0;width:604px;top:92px;text-align:center;font-size:22px;font-weight:600;letter-spacing:1px;color:#45454b}
.page{position:absolute;overflow:hidden}
.page-left{left:21px;top:194px;width:585px;height:1006px;background:var(--white);box-shadow:0 4px 18px rgba(0,0,0,.08)}
.page-right{left:600px;top:0;width:589px;height:1126px;background:var(--white);box-shadow:0 4px 18px rgba(0,0,0,.08)}
.photo{position:absolute;inset:0}
/* hero */
.hero{left:0;top:0;width:585px;height:280px}
.hero .photo{background:linear-gradient(180deg,#5c4c62 0%,#b77a84 18%,#8d7880 32%,#55504f 55%,#3b3532 80%,#4e5645 100%)}
.nav{left:69px;top:14px;right:80px;height:12px;color:#fff;display:flex;align-items:center}
.nav .logo{font-size:9px;font-weight:600;letter-spacing:.3px}
.nav .phone{font-size:4.5px;margin-left:18px;opacity:.9}
.nav .social{display:flex;gap:7px;margin-left:60px}
.nav .social span{width:5px;height:5px;border-radius:50%;background:#fff;display:block}
.nav .links{margin-left:auto;display:flex;gap:14px;font-size:4.8px;font-weight:600}
.burger{left:527px;top:18px;width:9px}
.burger i{display:block;height:1px;background:#fff;margin-bottom:2px}
.hero-num{left:69px;top:175px;font-size:38px;font-weight:800;color:#fff}
.dots{left:69px;top:219px;display:flex;gap:4px}
.dots i{width:10px;height:1.5px;background:rgba(255,255,255,.6)}
.dots i.on{background:#fff}
.hero-name{left:69px;top:228px;font-size:19px;font-weight:700;color:#fff}
.btn-red{background:var(--red);color:#fff;font-weight:700;display:flex;align-items:center;justify-content:center;box-shadow:0 2px 5px rgba(0,0,0,.2)}
.hero-btn{left:69px;top:267px;width:87px;height:22px;font-size:5.5px;letter-spacing:.4px}
/* faint headings */
.ghost{font-family:'Playfair Display',serif;font-weight:700;color:var(--faint);white-space:nowrap}
.feat-ghost{left:8px;top:310px;font-size:66px}
.feat-title{left:69px;top:346px;font-size:20px;line-height:21px;font-weight:400}
.feat-sub{left:69px;top:394px;font-size:6px;font-weight:600;color:var(--red)}
.feat-text{left:69px;top:410px;width:125px;font-size:5.3px;line-height:9.3px;color:#6a6a70}
.arrow-l{left:112px;top:486px}
.card-img{position:absolute}
.card-buy{width:40px;height:19px;font-size:5px}
.card-cap{font-size:6.8px;font-weight:600}
.card-sub{font-size:4.2px;color:var(--muted)}
/* tiles */
.tile{position:absolute;overflow:hidden}
.tile .shade{position:absolute;inset:0;background:linear-gradient(180deg,rgba(0,0,0,0) 30%,rgba(0,0,0,.45) 100%)}
.tag{position:absolute;background:var(--red);color:#fff;font-size:4.3px;font-weight:700;padding:2px 5px}
.tile .info{position:absolute;left:20px;bottom:16px;color:#fff}
.info .price{font-size:9.5px;font-weight:700}
.info .ttl{font-size:7.5px;font-weight:600;margin-top:2px}
.info .desc{font-size:4.4px;line-height:7.5px;margin-top:5px;width:170px;opacity:.9}
/* high-rise */
.rise-left{left:0;top:883px;width:585px;height:123px;background:#f4f4f6}
.rise-right{left:6px;top:216px;width:583px;height:234px;background:var(--panel)}
.rise-right .beam{position:absolute;left:-20px;top:0;width:180px;height:234px;background:#e4e4e8;clip-path:polygon(0 0,100% 0,70% 100%,0 100%)}
.rise-right .beam2{position:absolute;left:240px;top:0;width:120px;height:234px;background:#f3f3f5;clip-path:polygon(40% 0,100% 0,60% 100%,0 100%)}
.tower{background:linear-gradient(160deg,#2b3544 0%,#5a6a80 30%,#9aa3ad 55%,#d9dde0 70%,#5b6068 100%)}
.rise-ghost{font-size:34px;color:#e6e6ea}
.rise-h{font-size:12.5px;font-weight:400;color:#333}
.rise-sub{font-size:7.5px;font-weight:700}
.rise-line{height:1.5px;background:var(--red);width:108px}
.rise-text{font-size:4.8px;line-height:8.6px;color:#6a6a70;width:160px}
.amen{font-size:4.8px;display:flex;align-items:center;gap:4px;color:#444}
.amen svg{width:7px;height:7px}
.nav-btn{width:19px;height:17px;display:flex;align-items:center;justify-content:center}
/* posts */
.posts-ghost{left:120px;top:454px;font-size:66px}
.posts-title{left:0;width:589px;top:475px;text-align:center;font-size:19px;font-weight:400}
.filter{font-size:5.8px;font-weight:600}
.select{height:12px;border:1px solid #e3e3e6;font-size:4.5px;color:#888;display:flex;align-items:center;justify-content:space-between;padding:0 4px}
.search-line{left:70px;top:535px;width:448px;height:1px;background:#ebebee}
.post-img{position:absolute;width:142px;height:152px}
.post-btn{position:absolute;width:52px;height:20px;font-size:5.2px}
.post-price{font-size:6.5px;font-weight:500}
.post-addr{font-size:4.3px;color:var(--muted)}
/* footer */
.footer{left:6px;top:986px;width:583px;height:140px;background:var(--foot);border-top:1px solid #ececef}
.foot-logo{font-size:8px;font-weight:500;color:var(--red)}
.foot-h{font-size:5.2px;font-weight:600}
.foot-list{font-size:4.6px;color:#8a8a92;line-height:10.3px}
.soc{display:flex;align-items:center;gap:4px;font-size:4.6px;color:#8a8a92;height:17px}
.soc i{width:9px;height:9px;border-radius:50%;display:block}
.legal{font-size:4.3px;color:#8a8a92}
</style>
</head>
<body>

<div class="abs brand-title">PLUSH DWELLINGS</div>

<!-- LEFT PAGE -->
<section class="page page-left">
  <div class="abs hero">
    <div class="photo" role="img" aria-label="Stone manor house at dusk with warm lit windows under a pink sky"></div>
    <div class="abs nav">
      <span class="logo">PLUSH DWELLINGS</span>
      <span class="phone">☏ +1(02) 555 0148</span>
      <span class="social"><span></span><span></span><span></span><span></span></span>
      <span class="links"><span>OUR PROPERTIES</span><span>PLATINUM CLUB</span></span>
    </div>
    <div class="abs burger"><i></i><i></i><i></i></div>
    <div class="abs hero-num">02</div>
    <div class="abs dots"><i></i><i class="on"></i><i></i></div>
    <div class="abs hero-name">Luxury Palace</div>
  </div>
  <div class="abs btn-red hero-btn">SEARCH ALL HOMES</div>

  <div class="abs ghost feat-ghost">Featured</div>
  <div class="abs feat-title">Featured<br>Home</div>
  <div class="abs feat-sub">Dummy text of the printing etting</div>
  <div class="abs feat-text">Lorem ipsum dolor sit amet, consectetur adipisicing elit, sed do eiusmod tempor incididunt ut labore et dolore magna aliqua. Ut enim ad minim veniam, quis nostrud exercitation.</div>
  <svg class="abs arrow-l" width="40" height="14" viewBox="0 0 40 14">
    <circle cx="7" cy="7" r="6" fill="none" stroke="#aaa" stroke-width=".8"/>
    <path d="M8.5 4.5 6 7l2.5 2.5" fill="none" stroke="#aaa" stroke-width=".8"/>
    <circle cx="30" cy="7" r="6" fill="none" stroke="#333" stroke-width=".9"/>
    <path d="M21 7h12M30 4l3 3-3 3" fill="none" stroke="#333" stroke-width=".9"/>
  </svg>

  <div class="card-img" style="left:219px;top:331px;width:136px;height:165px;background:linear-gradient(180deg,#c7d0d6 0%,#6f6a55 35%,#8a5a2e 60%,#f3f4f6 80%)" role="img" aria-label="Timber chalet in snowy pine forest"></div>
  <div class="abs btn-red card-buy" style="left:309px;top:485px">BUY</div>
  <div class="abs card-cap" style="left:219px;top:511px">Location/Geneva</div>
  <div class="abs card-sub" style="left:219px;top:524px">Deposit of32in basement</div>

  <div class="card-img" style="left:367px;top:331px;width:136px;height:165px;background:linear-gradient(180deg,#eef0f2 0%,#d9d6d2 40%,#9e8b7c 70%,#5a3e34 100%)" role="img" aria-label="Grand white foyer with double staircase"></div>
  <div class="abs btn-red card-buy" style="left:457px;top:485px">BUY</div>
  <div class="abs card-cap" style="left:367px;top:511px">Sale/Vucherens</div>
  <div class="abs card-sub" style="left:367px;top:524px">On plans - Spacious contiguous villa of4.5</div>

  <div class="card-img" style="left:515px;top:331px;width:70px;height:165px;background:linear-gradient(180deg,#e7eaec 0%,#d6dcd8 50%,#8ea08b 100%)" role="img" aria-label="White Mediterranean villa with palms"></div>
  <div class="abs card-cap" style="left:515px;top:511px">Location/Geneva</div>
  <div class="abs card-sub" style="left:515px;top:524px">Deposit of32in basement</div>

  <div class="tile" style="left:0;top:571px;width:293px;height:175px">
    <div class="photo" style="background:linear-gradient(135deg,#6b4a32 0%,#3d2e26 40%,#8a7a68 75%,#5b4d40 100%)" role="img" aria-label="Warm modern living room with wood ceiling"></div>
    <div class="shade"></div><div class="tag" style="left:20px;top:18px">FEATURED</div>
    <div class="info"><div class="price">$2,5900.00</div><div class="ttl">Lorem ipsum is simply dummy text</div><div class="desc">Lorem ipsum is simply dummy text of the printing and typesetting industry. Lorem Ipsum has been the.</div></div>
  </div>
  <div class="tile" style="left:293px;top:571px;width:292px;height:175px">
    <div class="photo" style="background:linear-gradient(180deg,#7a8a90 0%,#5a4434 35%,#2f4450 65%,#1f3440 100%)" role="img" aria-label="Stone lodge beside a reflecting pool at dusk"></div>
    <div class="shade"></div><div class="tag" style="left:20px;top:18px">FEATURED</div>
    <div class="info"><div class="price">$2,5900.00</div><div class="ttl">Lorem ipsum is simply dummy text</div><div class="desc">Lorem ipsum is simply dummy text of the printing and typesetting industry. Lorem Ipsum has been the.</div></div>
  </div>
  <div class="tile" style="left:0;top:746px;width:195px;height:137px">
    <div class="photo" style="background:linear-gradient(135deg,#c9b8a2 0%,#6b5a4a 45%,#3a302a 100%)" role="img" aria-label="Dining room with chandelier"></div>
    <div class="shade"></div><div class="tag" style="left:20px;top:18px">FEATURED</div>
    <div class="info"><div class="price">$2,5900.00</div><div class="ttl">Lorem ipsum is simply dumm</div><div class="desc" style="width:140px">Lorem ipsum is simply dummy text of the printing and typesetting industry. Lorem Ips.</div></div>
  </div>
  <div class="tile" style="left:195px;top:746px;width:195px;height:137px">
    <div class="photo" style="background:linear-gradient(180deg,#6a6fa8 0%,#9a8fb8 35%,#5a5468 65%,#3f4a3a 100%)" role="img" aria-label="Suburban house under violet evening sky"></div>
    <div class="shade"></div><div class="tag" style="left:20px;top:18px">FEATURED</div>
    <div class="info"><div class="price">$2,5900.00</div><div class="ttl">Lorem Ipsum is simply dumm</div><div class="desc" style="width:140px">Lorem ipsum is simply dummy text of the printing and typesetting industry. Lorem Ips.</div></div>
  </div>
  <div class="tile" style="left:390px;top:746px;width:195px;height:137px">
    <div class="photo" style="background:linear-gradient(180deg,#6f7c86 0%,#4a3a30 40%,#b0743a 65%,#3a4530 100%)" role="img" aria-label="Round modern house with wraparound balcony"></div>
    <div class="shade"></div><div class="tag" style="left:20px;top:18px">FEATURED</div>
    <div class="info"><div class="price">$2,5900.00</div><div class="ttl">Lorem Ipsum is simply dumm</div><div class="desc" style="width:140px">Lorem ipsum is simply dummy text of the printing and typesetting industry. Lorem Ips.</div></div>
  </div>

  <div class="abs rise-left"></div>
  <div class="abs tower" style="left:69px;top:922px;width:256px;height:84px" role="img" aria-label="Glass skyscrapers against a pale sky"></div>
  <div class="abs ghost rise-ghost" style="left:340px;top:896px">High rise</div>
  <div class="abs rise-h" style="left:357px;top:918px">Heigh-Rise Devision</div>
  <div class="abs rise-sub" style="left:359px;top:944px">Homert Appartment</div>
  <div class="abs rise-line" style="left:359px;top:958px"></div>
  <div class="abs rise-text" style="left:359px;top:970px">Lorem Ipsum is simply dummy text of the printing and typesetting industry. Lorem Ips.um has been the industry's standard dummy text ever since the 1500s.</div>
</section>

<!-- RIGHT PAGE -->
<section class="page page-right">
  <div class="tile" style="left:0;top:0;width:294px;height:78px">
    <div class="photo" style="background:linear-gradient(135deg,#6b4a32 0%,#3d2e26 40%,#8a7a68 75%,#5b4d40 100%)" role="img" aria-label="Warm modern living room"></div>
    <div class="shade"></div>
    <div class="info" style="bottom:18px"><div class="price">$2,5900.00</div><div class="ttl">Lorem ipsum is simply dummy text</div><div class="desc">Lorem ipsum is simply dummy text of the printing and typesetting industry. Lorem Ipsum has been the.</div></div>
  </div>
  <div class="tile" style="left:294px;top:0;width:295px;height:78px">
    <div class="photo" style="background:linear-gradient(180deg,#5a4434 0%,#2f4450 55%,#1f3440 100%)" role="img" aria-label="Stone lodge beside a pool"></div>
    <div class="shade"></div>
    <div class="info" style="bottom:18px"><div class="price">$2,5900.00</div><div class="ttl">Lorem ipsum is simply dummy text</div><div class="desc">Lorem ipsum is simply dummy text of the printing and typesetting industry. Lorem Ipsum has been the.</div></div>
  </div>
  <div class="tile" style="left:0;top:78px;width:196px;height:138px">
    <div class="photo" style="background:linear-gradient(135deg,#c9b8a2 0%,#6b5a4a 45%,#3a302a 100%)" role="img" aria-label="Dining room with chandelier"></div>
    <div class="shade"></div><div class="tag" style="left:20px;top:18px">FEATURED</div>
    <div class="info"><div class="price">$2,5900.00</div><div class="ttl">Lorem Ipsum is simply dumm</div><div class="desc" style="width:140px">Lorem ipsum is simply dummy text of the printing and typesetting industry. Lorem Ips.</div></div>
  </div>
  <div class="tile" style="left:196px;top:78px;width:197px;height:138px">
    <div class="photo" style="background:linear-gradient(180deg,#6a6fa8 0%,#9a8fb8 35%,#5a5468 65%,#3f4a3a 100%)" role="img" aria-label="Suburban house under violet evening sky"></div>
    <div class="shade"></div><div class="tag" style="left:20px;top:18px">FEATURED</div>
    <div class="info"><div class="price">$2,5900.00</div><div class="ttl">Lorem Ipsum is simply dumm</div><div class="desc" style="width:140px">Lorem ipsum is simply dummy text of the printing and typesetting industry. Lorem Ips.</div></div>
  </div>
  <div class="tile" style="left:393px;top:78px;width:196px;height:138px">
    <div class="photo" style="background:linear-gradient(180deg,#6f7c86 0%,#4a3a30 40%,#b0743a 65%,#3a4530 100%)" role="img" aria-label="Round modern house with balcony"></div>
    <div class="shade"></div><div class="tag" style="left:20px;top:18px">FEATURED</div>
    <div class="info"><div class="price">$2,5900.00</div><div class="ttl">Lorem Ipsum is simply dumm</div><div class="desc" style="width:140px">Lorem ipsum is simply dummy text of the printing and typesetting industry. Lorem Ips.</div></div>
  </div>

  <div class="abs rise-right"><div class="beam"></div><div class="beam2"></div></div>
  <div class="abs tower" style="left:70px;top:256px;width:258px;height:156px" role="img" aria-label="Glass skyscrapers against a pale sky"></div>
  <div class="abs btn-red nav-btn" style="left:309px;top:388px"><svg width="8" height="6" viewBox="0 0 8 6"><path d="M8 3H1M3 1 1 3l2 2" fill="none" stroke="#fff" stroke-width=".8"/></svg></div>
  <div class="abs nav-btn" style="left:328px;top:388px;background:var(--dark)"><svg width="8" height="6" viewBox="0 0 8 6"><path d="M0 3h7M5 1l2 2-2 2" fill="none" stroke="#fff" stroke-width=".8"/></svg></div>
  <div class="abs ghost rise-ghost" style="left:340px;top:226px">High rise</div>
  <div class="abs rise-h" style="left:359px;top:251px">Heigh-Rise Devision</div>
  <div class="abs rise-sub" style="left:361px;top:282px">Homert Appartment</div>
  <div class="abs rise-line" style="left:361px;top:294px"></div>
  <div class="abs rise-text" style="left:361px;top:305px;width:160px">Lorem Ipsum is simply dummy text of the printing and typesetting industry. Lorem Ips.um has been the industry's standard dummy text ever since the 1500s.</div>
  <div class="abs amen" style="left:361px;top:342px"><svg viewBox="0 0 8 8"><path d="M1 4h6M2 2v4M6 2v4" stroke="#d42b2b" fill="none"/></svg>Gymnasium</div>
  <div class="abs amen" style="left:434px;top:342px"><svg viewBox="0 0 8 8"><rect x="1" y="2" width="6" height="5" stroke="#d42b2b" fill="none"/></svg>Power backup</div>
  <div class="abs amen" style="left:361px;top:358px"><svg viewBox="0 0 8 8"><path d="M1 7V3l3-2 3 2v4z" stroke="#d42b2b" fill="none"/></svg>Community hall</div>
  <div class="abs amen" style="left:434px;top:358px"><svg viewBox="0 0 8 8"><path d="M2 1v6M6 1v6M2 3h4M2 5h4" stroke="#d42b2b" fill="none"/></svg>Swimming pool</div>
  <div class="abs amen" style="left:361px;top:374px"><svg viewBox="0 0 8 8"><circle cx="4" cy="3.5" r="2.5" stroke="#d42b2b" fill="none"/><path d="M4 6v2" stroke="#d42b2b"/></svg>Garden</div>

  <div class="abs ghost posts-ghost">Posts</div>
  <div class="abs posts-title">Latest Posts</div>
  <div class="abs filter" style="left:70px;top:522px">Type</div>
  <div class="abs select" style="left:93px;top:519px;width:65px">Luxury Real Estate <span>⌄</span></div>
  <div class="abs filter" style="left:183px;top:522px">Purpose</div>
  <div class="abs select" style="left:214px;top:519px;width:42px">To Buy <span>⌄</span></div>
  <div class="abs" style="left:478px;top:526px;font-size:4.5px;color:#999">Search...</div>
  <svg class="abs" style="left:511px;top:524px" width="7" height="7" viewBox="0 0 7 7"><circle cx="3" cy="3" r="2.2" fill="none" stroke="#333" stroke-width=".8"/><path d="M4.6 4.6 6.6 6.6" stroke="#333" stroke-width=".8"/></svg>
  <div class="abs search-line"></div>

  <div class="post-img" style="left:70px;top:557px;background:linear-gradient(180deg,#e9ecef 0%,#cfd6d3 55%,#7a9080 100%)" role="img" aria-label="White villa with arched windows and palms"></div>
  <div class="post-img" style="left:224px;top:557px;background:linear-gradient(180deg,#b89a4a 0%,#d9b8c2 40%,#c7a2ae 70%,#4a6a3e 100%)" role="img" aria-label="Pink townhouse facade"></div>
  <div class="post-img" style="left:377px;top:557px;background:linear-gradient(180deg,#e7eef3 0%,#c2ccd3 50%,#6d7a6a 100%)" role="img" aria-label="Modern white house with glass balcony"></div>
  <div class="post-img" style="left:70px;top:764px;background:linear-gradient(180deg,#b8244a 0%,#e8e8ea 35%,#2a5fb8 70%,#e0e0e2 100%)" role="img" aria-label="White wall with blue door and flowers"></div>
  <div class="post-img" style="left:224px;top:764px;background:linear-gradient(180deg,#c55a4a 0%,#f2f2f4 35%,#e6e6ea 100%)" role="img" aria-label="White gabled houses with red roofs"></div>
  <div class="post-img" style="left:377px;top:764px;background:linear-gradient(180deg,#d8e0e6 0%,#c4b8a0 45%,#6f8f4a 75%,#4f7a35 100%)" role="img" aria-label="Single storey house with lawn"></div>

  <div class="abs btn-red post-btn" style="left:150px;top:694px">BUY NOW</div>
  <div class="abs btn-red post-btn" style="left:304px;top:694px">BUY NOW</div>
  <div class="abs btn-red post-btn" style="left:457px;top:694px">BUY NOW</div>
  <div class="abs btn-red post-btn" style="left:150px;top:902px">BUY NOW</div>
  <div class="abs btn-red post-btn" style="left:304px;top:902px">BUY NOW</div>
  <div class="abs btn-red post-btn" style="left:457px;top:902px">BUY NOW</div>

  <div class="abs post-price" style="left:70px;top:718px">$1,435,000</div><div class="abs post-addr" style="left:70px;top:732px">Bustan - Regerdengor 25A Colony</div>
  <div class="abs post-price" style="left:224px;top:718px">$1,435,000</div><div class="abs post-addr" style="left:224px;top:732px">Bustan - Regerdengor 25A Colony</div>
  <div class="abs post-price" style="left:377px;top:718px">$1,435,000</div><div class="abs post-addr" style="left:377px;top:732px">Bustan - Regerdengor 25A Colony</div>
  <div class="abs post-price" style="left:70px;top:925px">$1,435,000</div><div class="abs post-addr" style="left:70px;top:939px">Bustan - Regerdengor 25A Colony</div>
  <div class="abs post-price" style="left:224px;top:925px">$1,435,000</div><div class="abs post-addr" style="left:224px;top:939px">Bustan - Regerdengor 25A Colony</div>
  <div class="abs post-price" style="left:377px;top:925px">$1,435,000</div><div class="abs post-addr" style="left:377px;top:939px">Bustan - Regerdengor 25A Colony</div>

  <footer class="abs footer">
    <div class="abs foot-logo" style="left:64px;top:24px">PLUSH DWELLINGS</div>
    <div class="abs foot-h" style="left:151px;top:22px">ABOUT US</div>
    <div class="abs foot-list" style="left:151px;top:34px">Pricing<br>Press room<br>Stories &amp; Trends<br>Careers<br>Site map<br>Affiliates</div>
    <div class="abs foot-h" style="left:225px;top:22px">SERVICES</div>
    <div class="abs foot-list" style="left:225px;top:34px">Management<br>Brokerage<br>Promotions<br>Condo</div>
    <div class="abs foot-h" style="left:300px;top:22px">TOOLS</div>
    <div class="abs foot-list" style="left:300px;top:34px">Online perview<br>Search<br>Gallery<br>Top 10<br>Etc</div>
    <div class="abs foot-h" style="left:375px;top:22px">OUR SOCIAL LINKS</div>
    <div class="abs" style="left:375px;top:34px">
      <div class="soc"><i style="background:#3b5998"></i>Friendsheet</div>
      <div class="soc"><i style="background:#2aa3ef"></i>Chirper</div>
      <div class="soc"><i style="background:#d42b2b"></i>Pinboard</div>
    </div>
    <div class="abs" style="left:450px;top:34px">
      <div class="soc"><i style="background:#0e76a8"></i>Workline</div>
      <div class="soc"><i style="background:#e0533f"></i>Circle Plus</div>
      <div class="soc"><i style="background:#f5a623"></i>RSS Feeds</div>
    </div>
    <div class="abs legal" style="left:64px;top:121px">Terms of Service · Privacy Policy · Contact · © 2018 Plush Dwellings</div>
    <div class="abs legal" style="left:464px;top:121px">Language</div>
    <div class="abs select" style="left:490px;top:118px;width:22px;height:10px">EN <span>⌄</span></div>
  </footer>
</section>

</body>
</html>
```